Business Card template designs

We need a lot of Business card designs.
Your designs will get exposure on our newly opened business-card printing website.
We are committed to quality of paper and packages we use, so they will come up very fancy.

Here is your advantage. We will put the profile of the graphic designer on our site so that you can showcase your designs to people around the world and in Japan.

A profile is not mandatory, although we encourage graphic designers to have a profile to get continuous work in the future.
We are looking forward to having many good designs.

The right of the use of design will be owned by us.
The design may be used to the products other than
business cards.

Target Market(s)

designer,photographer,creator,artist

Industry/Entity Type

Printing

Contact Information for Business Card

The back design is important.
Please check the reference file.

Requirements
Must have
• Please include the following, required information on your business card designs.
• Name: Haruna Okabe
• Title: Designer
• Web: https://www.ketori.co.jp/kt/
• Address: 4-17 Kamiharuta-Cho Meguro-ku, Tokyo
• Email: info@kketori.com
• Phone: 03 4816 3907
• Mobile: 070 2143 6658
• * For Japanese sites, we will convert the text portion to Japanese characters.
• * In case of 28mmx70mm only include Name,Enail,Phone and SNS account(https://www.facebook.com/kketori.com)
• 1. colorful
• 2. simple
• 3. natural
• 4. modern
• 5. cool
• 6. sporty
• Please make variations of the same image with 3-6
• different colors / patterns for one design so that
• customers can compare and choose.
• If you want to use a same picture, please make make
• copies and paste on each different types of design.
Nice to have
• You may also use, the following non-required information.
• Company Name: Ketori, Inc.
• Fax: 03-4173-9620
• Open space for company logo

```html
<!DOCTYPE html>
<html lang="en">
<head>
<meta charset="utf-8">
<title>Haruna Okabe – Business Card</title>
<link rel="stylesheet" href="https://fonts.googleapis.com/css2?family=PT+Sans:wght@400;700&display=swap">
<style>
  :root {
    --page-bg: #ece7e0;
    --wood-light: #b08766;
    --wood-mid: #a27a5b;
    --wood-dark: #8f6a4e;
    --ink: #2a1e15;
    --emblem: #7e5c43;
  }
  html, body {
    margin: 0;
    padding: 0;
    width: 1200px;
    height: 848px;
    overflow: hidden;
    background: var(--page-bg);
  }
  .canvas {
    position: relative;
    width: 1200px;
    height: 848px;
  }
  .card {
    position: absolute;
    left: 100px;
    top: 121px;
    width: 1000px;
    height: 606px;
    border-radius: 62px;
    background:
      repeating-linear-gradient(100deg, rgba(255,255,255,0.04) 0 3px, rgba(0,0,0,0.03) 3px 7px),
      linear-gradient(135deg, var(--wood-light), var(--wood-mid) 55%, var(--wood-dark));
    box-shadow: 0 6px 0 #4a372a, 0 14px 30px rgba(0,0,0,0.18);
    font-family: "PT Sans", sans-serif;
    color: var(--ink);
  }
  .emblem-area {
    position: absolute;
    left: 590px;
    top: 30px;
    width: 250px;
    height: 250px;
  }
  .identity {
    position: absolute;
    left: 150px;
    top: 250px;
  }
  .identity .name {
    margin: 0;
    font-size: 46px;
    font-weight: 400;
    letter-spacing: 0.5px;
  }
  .identity .title {
    margin: 4px 0 0 22px;
    font-size: 27px;
    font-weight: 700;
    letter-spacing: 0.5px;
  }
  .contacts {
    position: absolute;
    left: 240px;
    top: 365px;
    margin: 0;
    padding: 0;
    list-style: none;
    font-size: 27px;
    line-height: 41px;
  }
  .contacts li {
    display: flex;
    align-items: center;
    gap: 16px;
  }
  .contacts svg {
    width: 24px;
    height: 24px;
    flex: none;
    fill: var(--ink);
  }
</style>
</head>
<body>
<div class="canvas">
  <section class="card">
    <svg class="emblem-area" viewBox="0 0 250 250" role="img" aria-label="Cut-out leaf emblem decoration">
      <path d="M20 70 C70 60 110 100 150 190 C170 210 200 200 230 120 C240 80 220 20 200 0 C150 30 120 40 60 40 C40 45 25 55 20 70 Z" fill="var(--emblem)" opacity="0.55"/>
    </svg>

    <div class="identity">
      <h1 class="name">Haruna Okabe</h1>
      <p class="title">Designer</p>
    </div>

    <ul class="contacts">
      <li>
        <svg viewBox="0 0 24 24" aria-hidden="true"><path d="M2 8c0-2 3-4 10-4s10 2 10 4v2h-5V8H7v2H2z"/><rect x="4" y="12" width="16" height="9" rx="1.5"/></svg>
        <span>03 4816 3907</span>
      </li>
      <li>
        <svg viewBox="0 0 24 24" aria-hidden="true"><path d="M7 1h10a2 2 0 0 1 2 2v18a2 2 0 0 1-2 2H7a2 2 0 0 1-2-2V3a2 2 0 0 1 2-2zm0 3v14h10V4z"/></svg>
        <span>070 2143 6658</span>
      </li>
      <li>
        <svg viewBox="0 0 24 24" aria-hidden="true"><rect x="6" y="2" width="10" height="7"/><rect x="2" y="9" width="20" height="10" rx="1.5"/><rect x="6" y="15" width="10" height="7"/></svg>
        <span>info@kketori.com</span>
      </li>
      <li>
        <svg viewBox="0 0 24 24" aria-hidden="true"><path d="M2 5h20v14H2z M3.5 6.5 12 13l8.5-6.5" stroke="var(--wood-mid)" stroke-width="1.4"/></svg>
        <span>www.ketori.co.jp/kt/</span>
      </li>
      <li>
        <svg viewBox="0 0 24 24" aria-hidden="true"><path d="M12 1a7 7 0 0 1 7 7c0 5-7 14-7 14S5 13 5 8a7 7 0 0 1 7-7zm0 4a3 3 0 1 0 0 6 3 3 0 0 0 0-6z"/></svg>
        <span>4-17 Kamiharuta-Cho Meguro-ku, Tokyo</span>
      </li>
    </ul>
  </section>
</div>
</body>
</html>
```